Finance Broker helping people meet their personal and business goals

New business card design,
1st look at the old business card so this makes sense.
I DON'T want:
the subtext "For all your Rural and Commercial Finance".
I DON'T want the: "and Management Consultant" words
I DON'T want the old phone: 07 48213957
I DON'T want the fax number: 07 45826031
I DON'T want the email address: tallowcreek@brightlink.com.au
I DON'T want the flower
What I DO want
I DO want the mobile 0451 836 209 (in larger text)
I DO want:
My name: Dennis Harwell-Lowe
I DO want: Australian Credit Licence 529164 (Tallow Creek Pty Ltd)
I DO want: Principal Finance Broker
I DO want new email: dennis@plotnextstep.com.au
I DO want address: PO Box 928, Tully Qld 4854
I DO want the existing logo (PNS on existing card)

Target Market(s)

Business Borrowers, Home Purchasers, and People wanting to finance cars and plant and equipment

Industry/Entity Type

Financial Service

Contact Information for Business Card

See project description

Font styles to use
Serif

Colors

Designer to choose colors to be used in the design.

Requirements
Must have
• See project description
Nice to have
• Black and Yellow colours
Should not have
• See project description

```html
<!DOCTYPE html>
<html lang="en">
<head>
<meta charset="utf-8">
<title>Plot Next Step – Business Cards</title>
<link href="https://fonts.googleapis.com/css2?family=Open+Sans:wght@400;600;700&display=swap" rel="stylesheet">
<style>
  :root {
    --bg: #d9dcdf;
    --card: #2a2d33;
    --yellow: #f3ea3c;
    --amber: #e4a21c;
    --white: #f4f4f4;
  }
  * { margin: 0; padding: 0; box-sizing: border-box; }
  html, body { width: 1200px; height: 800px; overflow: hidden; }
  body {
    background: var(--bg);
    font-family: "Open Sans", Arial, sans-serif;
    color: var(--white);
    position: relative;
  }
  .card {
    position: absolute;
    left: 285px;
    width: 630px;
    height: 360px;
    background: var(--card);
    box-shadow: 0 6px 18px rgba(0,0,0,0.25);
  }
  .card--front { top: 25px; }
  .card--back { top: 415px; }

  .brand {
    display: flex;
    align-items: center;
    gap: 14px;
    color: var(--yellow);
    font-weight: 700;
  }
  .brand__dot {
    border-radius: 50%;
    background: var(--yellow);
    flex: none;
  }

  /* Front */
  .card--front .brand {
    position: absolute;
    top: 120px;
    left: 0; right: 0;
    justify-content: center;
    font-size: 44px;
  }
  .card--front .brand__dot { width: 40px; height: 40px; }
  .tagline {
    position: absolute;
    top: 236px;
    left: 40px; right: 40px;
    display: flex;
    align-items: center;
    gap: 12px;
    font-size: 15px;
    white-space: nowrap;
  }
  .tagline__rule { flex: 1; height: 2px; background: var(--amber); }

  /* Back */
  .card--back .brand {
    position: absolute;
    top: 132px;
    left: 28px;
    width: 240px;
    flex-direction: column;
    gap: 10px;
    font-size: 27px;
    text-align: center;
  }
  .card--back .brand__dot { width: 44px; height: 44px; }
  .divider {
    position: absolute;
    left: 292px;
    top: 90px;
    width: 2px;
    height: 160px;
    background: var(--amber);
  }
  .contact {
    position: absolute;
    left: 312px;
    top: 86px;
    right: 20px;
  }
  .contact__name { color: var(--yellow); font-weight: 700; font-size: 23px; line-height: 1.2; }
  .contact__role { font-size: 14px; line-height: 1.35; }
  .contact__list { list-style: none; margin-top: 12px; }
  .contact__item { display: flex; align-items: center; gap: 8px; font-size: 14px; line-height: 1.5; }
  .contact__item--phone { font-size: 21px; line-height: 1.3; }
  .contact__item svg { width: 14px; height: 14px; flex: none; }
  .address {
    position: absolute;
    bottom: 30px;
    left: 0; right: 0;
    text-align: center;
    font-size: 16px;
  }
</style>
</head>
<body>

<section class="card card--front">
  <div class="brand">
    <span class="brand__dot"></span>
    <span class="brand__name">Plot Next Step</span>
  </div>
  <div class="tagline">
    <span class="tagline__rule"></span>
    <span class="tagline__text">A Member of the Tallow Creek Group</span>
    <span class="tagline__rule"></span>
  </div>
</section>

<section class="card card--back">
  <div class="brand">
    <span class="brand__dot"></span>
    <span class="brand__name">Plot Next Step</span>
  </div>
  <div class="divider"></div>
  <div class="contact">
    <p class="contact__name">Dennis Harwell-Lowe</p>
    <p class="contact__role">Australian Credit Licence 529164<br>(Tallow Creek Pty Ltd)<br>Principal Finance Broker</p>
    <ul class="contact__list">
      <li class="contact__item contact__item--phone">
        <svg viewBox="0 0 14 14" aria-hidden="true"><rect x="3" y="0.8" width="8" height="12.4" rx="1.5" fill="none" stroke="#e4a21c" stroke-width="1.4"/><circle cx="7" cy="10.8" r="0.8" fill="#e4a21c"/></svg>
        0451 836 209
      </li>
      <li class="contact__item">
        <svg viewBox="0 0 14 14" aria-hidden="true"><rect x="0.8" y="2.5" width="12.4" height="9" fill="none" stroke="#e4a21c" stroke-width="1.4"/><path d="M1 3 L7 8 L13 3" fill="none" stroke="#e4a21c" stroke-width="1.4"/></svg>
        dennis@plotnextstep.com.au
      </li>
      <li class="contact__item">
        <svg viewBox="0 0 14 14" aria-hidden="true"><circle cx="7" cy="7" r="6" fill="none" stroke="#e4a21c" stroke-width="1.3"/><ellipse cx="7" cy="7" rx="2.6" ry="6" fill="none" stroke="#e4a21c" stroke-width="1.1"/><path d="M1 7 H13 M2 4 H12 M2 10 H12" stroke="#e4a21c" stroke-width="1"/></svg>
        www.plotnextstep.com.au
      </li>
    </ul>
  </div>
  <p class="address">PO Box 928, Tully Qld 4854</p>
</section>

</body>
</html>
```